Personal Training Studio business cards

Black logo on front. Also need: Carlyse Brondway Master Trainer, Phone: 0498315627 on the front.
On the back want the white logo and also want 10 stars or similar that can be stamped when attended Studio. The 10th start to have "Free" written under it.
Also want a line to write an appointment date and time on it.

```html
<!DOCTYPE html>
<html lang="en">
<head>
<meta charset="utf-8">
<title>Kestrel Studio – Business Cards</title>
<link rel="stylesheet" href="https://fonts.googleapis.com/css2?family=Lato:wght@400;700;900&display=swap">
<style>
  :root {
    --bg: #7c8888;
    --card-dark: #000000;
    --card-light: #f6f6f6;
    --purple: #6a3fa0;
    --green: #7cc242;
    --white: #ffffff;
    --ink: #1b1b1b;
  }
  * { box-sizing: border-box; margin: 0; padding: 0; }
  html, body { width: 1200px; height: 900px; overflow: hidden; }
  body {
    background: var(--bg);
    font-family: "Lato", sans-serif;
    position: relative;
  }
  .card {
    position: absolute;
    top: 170px;
    width: 340px;
    height: 560px;
    border-radius: 2px;
    box-shadow: 0 12px 30px rgba(0,0,0,0.25);
  }
  .card--front { left: 200px; background: var(--card-dark); }
  .card--back  { left: 660px; background: var(--card-light); }

  .brand {
    position: absolute;
    top: 70px;
    left: 0; right: 0;
    text-align: center;
  }
  .brand__name {
    display: flex;
    align-items: center;
    justify-content: center;
    gap: 10px;
    color: var(--purple);
    font-weight: 900;
    font-size: 34px;
    letter-spacing: 1px;
    text-transform: uppercase;
    line-height: 1.05;
  }
  .brand__dot {
    width: 16px; height: 16px;
    border-radius: 50%;
    background: var(--green);
    flex: none;
  }
  .brand__rule {
    width: 230px;
    height: 2px;
    margin: 8px auto 6px;
    background: var(--purple);
  }
  .brand__tagline {
    color: var(--green);
    font-weight: 700;
    font-size: 15px;
    letter-spacing: 1.5px;
  }

  /* front */
  .trainer {
    position: absolute;
    top: 360px;
    left: 0; right: 0;
    text-align: center;
  }
  .trainer__name {
    color: var(--white);
    font-weight: 900;
    font-size: 24px;
  }
  .trainer__role {
    color: var(--green);
    font-weight: 700;
    font-size: 19px;
    margin-top: 2px;
  }
  .contact {
    position: absolute;
    top: 455px;
    left: 0; right: 0;
    text-align: center;
  }
  .contact__icon { display: block; margin: 0 auto 8px; }
  .contact__phone {
    color: var(--white);
    font-weight: 900;
    font-size: 22px;
    letter-spacing: 1px;
  }

  /* back */
  .brand--back { top: 45px; }
  .stamps {
    position: absolute;
    top: 170px;
    left: 26px;
    width: 290px;
    height: 280px;
  }
  .stamp {
    position: absolute;
    width: 130px;
    height: 38px;
    border: 1.5px solid var(--green);
    background: var(--card-light);
    display: flex;
    align-items: center;
    padding-left: 8px;
    overflow: hidden;
  }
  .stamp__free {
    position: absolute;
    right: 0; bottom: 0;
    background: var(--green);
    color: var(--ink);
    font-weight: 900;
    font-size: 14px;
    padding: 2px 8px 1px 14px;
    clip-path: polygon(10px 0, 100% 0, 100% 100%, 0 100%);
  }
  .appointment {
    position: absolute;
    left: 30px; right: 30px;
    top: 465px;
  }
  .appointment__row {
    display: flex;
    align-items: flex-end;
    gap: 6px;
    height: 36px;
    color: var(--ink);
    font-weight: 700;
    font-size: 16px;
  }
  .appointment__line {
    flex: 1;
    border-bottom: 1.5px solid var(--ink);
    margin-bottom: 4px;
  }
</style>
</head>
<body>
  <svg width="0" height="0" style="position:absolute">
    <defs>
      <symbol id="star" viewBox="0 0 24 24">
        <polygon points="12,1 15,9 23,9 16.5,14 19,22 12,17 5,22 7.5,14 1,9 9,9" fill="#6a3fa0"/>
      </symbol>
    </defs>
  </svg>

  <section class="card card--front" aria-label="Business card front">
    <div class="brand">
      <div class="brand__name"><span class="brand__dot"></span>Kestrel Studio</div>
      <div class="brand__rule"></div>
      <div class="brand__tagline">Fitness Health Wellbeing</div>
    </div>
    <div class="trainer">
      <p class="trainer__name">Carlyse Brondway</p>
      <p class="trainer__role">Master Trainer</p>
    </div>
    <div class="contact">
      <svg class="contact__icon" width="40" height="40" viewBox="0 0 40 40" aria-hidden="true">
        <circle cx="20" cy="20" r="20" fill="#7cc242"/>
        <path d="M14 11c1-1 2.5-1 3 0l2 4c.4.9.1 1.8-.6 2.3l-1.4 1c1 2.4 2.8 4.3 5.2 5.4l1-1.4c.5-.7 1.5-1 2.3-.6l4 2c1 .5 1 2 0 3l-1.5 1.5c-1.5 1.5-4 1.6-6 .5-4.6-2.4-8.3-6.1-10.6-10.8-1-2-.8-4.4.8-5.9z" fill="#000"/>
      </svg>
      <p class="contact__phone">0498315627</p>
    </div>
  </section>

  <section class="card card--back" aria-label="Business card back, loyalty card">
    <div class="brand brand--back">
      <div class="brand__name"><span class="brand__dot"></span>Kestrel Studio</div>
      <div class="brand__rule"></div>
      <div class="brand__tagline">Fitness Health Wellbeing</div>
    </div>
    <div class="stamps">
      <div class="stamp" style="left:0;top:0"><svg width="22" height="22"><use href="#star"/></svg></div>
      <div class="stamp" style="left:0;top:50px"><svg width="22" height="22"><use href="#star"/></svg></div>
      <div class="stamp" style="left:0;top:100px"><svg width="22" height="22"><use href="#star"/></svg></div>
      <div class="stamp" style="left:0;top:150px"><svg width="22" height="22"><use href="#star"/></svg></div>
      <div class="stamp" style="left:0;top:200px"><svg width="22" height="22"><use href="#star"/></svg></div>
      <div class="stamp" style="left:156px;top:40px"><svg width="22" height="22"><use href="#star"/></svg></div>
      <div class="stamp" style="left:156px;top:90px"><svg width="22" height="22"><use href="#star"/></svg></div>
      <div class="stamp" style="left:156px;top:140px"><svg width="22" height="22"><use href="#star"/></svg></div>
      <div class="stamp" style="left:156px;top:190px"><svg width="22" height="22"><use href="#star"/></svg></div>
      <div class="stamp" style="left:156px;top:240px"><svg width="22" height="22"><use href="#star"/></svg><span class="stamp__free">FREE</span></div>
    </div>
    <div class="appointment">
      <div class="appointment__row"><span>Date</span><span class="appointment__line"></span></div>
      <div class="appointment__row"><span>Time</span><span class="appointment__line"></span></div>
    </div>
  </section>
</body>
</html>
```